Veterinary Service Needs Web Design

Pawdrena is a website that connects pet owners with veterinarians in their search area. I like clean, modern, but playful themes. Our service will be very similar to www.BrimQuel.com, however instead of doctors and human patients, our service is focused on veterinarians and pet owners/pets. If you are struggling to understand my idea, please visit www.brimquel.com and look how they organize the website. I would like something similar, yet unique, for Pawdrena. I have included the png file for the Pawdrena logo to this design request.

Home Page:
the home page must include a sign up button for pet owners to create an account, or to log in if they already have account. It must also include a search bar that will allow the user to search for veterinarians via company name, city/state, or zip code, and pick the date of when they would like to book an appointment.

Sign up/Log in Page:
I will need buttons that show an option to log in via Lumigram, or create an account with an email and password. If they are already a member, there should be a button that allows them to log in directly without having to register a new account.

Registration Page: I will need a form that captures the Pet Owner's first and last name, email address (this will also act as user name), password set up, phone number, home address, their pet's name, the breed of the pet, and the pet's birthday (month/year). There should be a button to 'replicate the form' if there is more than one pet they wish to tie to the account.

My Account Page: This page will show all appointments requested and all appointments confirmed. There will also need to be a button that allows the user to cancel the appointment. This page will also display all the information they entered when registering their account and will need a button that allows the user to edit their information.

Results Page:
This will be the page that displays the results of the veterinarians based on the input into the search bar from the home page. There will need to be a filter button that when clicked will bring up options to filter by appointment date request, distance, pet breed served, rating, and next available appointment. Each veterinarian displayed in the results list will need to have their company name, address, distance to user, rating, and a 'Select this veterinarian' button.

Selected Veterinarian from Results Page:
This page will be for when a pet owners clicks the veterinarian of their choice from the Results Page. This page will need to display all the information about that veterinarian - profile image, reviews/rating, address, distance to pet owner, along with all available time slots available for the date originally put into the search bar from the home page.

Veterinarian Log in/Sign up Page:
I will need the veterinarians to have a log in/sign up page. they will need to be able to sign up via email and set a password, or be able to log in directly if they already have an account.

Veterinarian Dashboard:
The veterinarian will need a dashboard which will display a calendar with all of their appointment requests. They will need to be able to click each appointment and click 'confirm' or 'deny'.

Closing Comments:
If you can think of any better UI/UX capabilities/ideas to improve efficiency and appeal, or any extra design ideas that would be appealing to the user, please incorporate this into your design proposals.

I completely understand this is web design and not a fully functioning website. I am asking the winning design to be coded with HTML/CSS, but fully understand it will not be fully functioning until it is coded by a full stack engineer.

Target Market(s)

Pet Owners and Veterinarians

Industry/Entity Type

Veterinary

Coding

Coded - Design and coding required

Number of Pages Required

5+ page

Colors
0054AA
0677BA
7BADD7
CADEEF
E8F1F8
0094D4
00A9DD
6FCCEA
C7EBF8
E9F6FB

Requirements
Must have
• Listed in the design brief.

```html
<!DOCTYPE html>
<html lang="en">
<head>
<meta charset="utf-8">
<title>Pawdrena – Book a Vet with a Tap</title>
<link href="https://fonts.googleapis.com/css2?family=Montserrat:ital,wght@0,400;0,500;0,600;0,700;1,400&family=Nunito:wght@800;900&display=swap" rel="stylesheet">
<style>
:root{
  --navy:#0054AA;
  --blue:#0677BA;
  --sky:#7BADD7;
  --pale:#CADEEF;
  --mist:#E8F1F8;
  --cyan:#0094D4;
  --aqua:#00A9DD;
  --light-aqua:#6FCCEA;
  --ice:#C7EBF8;
  --frost:#E9F6FB;
  --ink:#1d1d1d;
  --muted:#666;
  --star:#F2B300;
  --white:#fff;
}
*{margin:0;padding:0;box-sizing:border-box}
html,body{width:1200px;height:3582px;overflow:hidden;background:var(--white)}
body{position:relative;font-family:"Montserrat",sans-serif;color:var(--ink)}
.section{position:absolute;left:0;width:1200px}
.heading{font-family:"Nunito",sans-serif;font-weight:900;color:var(--navy);letter-spacing:-.3px}
.brand{font-family:"Montserrat",sans-serif;font-weight:700;color:var(--navy);display:flex;align-items:center;gap:10px}
.brand-dot{width:34px;height:34px;border-radius:50%;background:var(--navy)}
.btn{display:inline-flex;align-items:center;justify-content:center;border-radius:30px;font-weight:700;font-size:14px;text-transform:uppercase;letter-spacing:.3px}

/* hero */
.hero{top:0;height:521px;background:var(--pale)}
.hero-pattern{position:absolute;left:0;top:230px;width:1200px;height:291px;background:linear-gradient(180deg,rgba(123,173,215,0) 0%,rgba(123,173,215,.35) 100%)}
.hero .brand{position:absolute;left:145px;top:36px;font-size:46px}
.hero-actions{position:absolute;right:145px;top:42px;display:flex;gap:6px}
.btn-solid{background:var(--navy);color:var(--white);width:100px;height:44px}
.btn-outline{border:2px solid var(--navy);color:var(--navy);width:100px;height:44px}
.hero-title{position:absolute;top:170px;width:100%;text-align:center;font-size:58px}
.search{position:absolute;top:275px;left:190px;display:flex;gap:6px}
.field{height:38px;background:var(--white);border-radius:20px;display:flex;align-items:center;justify-content:space-between;padding:0 24px;font-size:10px;color:#444}
.field-company{width:448px}
.field-date{width:220px}
.btn-search{width:140px;height:38px;background:var(--ice);color:var(--navy);font-size:12px}
.scroll-notch{position:absolute;left:560px;bottom:0;width:80px;height:22px;background:var(--white);border-radius:40px 40px 0 0}

/* doctors */
.doctors{top:521px;height:559px}
.doctors-title{position:absolute;top:72px;width:100%;text-align:center;font-size:29px}
.card{position:absolute;background:var(--white);border-radius:4px;box-shadow:0 2px 12px rgba(0,0,0,.14);padding:26px 60px}
.card-main{top:163px;width:388px;height:262px}
.card-side{top:181px;width:300px;height:222px;padding:22px 50px}
.card-head{display:flex;align-items:center;gap:16px;margin-bottom:20px}
.avatar{width:64px;height:64px;border-radius:50%;background:linear-gradient(135deg,var(--sky),var(--navy))}
.card-side .avatar{width:56px;height:56px}
.doc-name{font-weight:600;font-size:16px}
.doc-city{font-style:italic;font-size:13px;color:var(--muted)}
.stars{color:var(--star);font-size:11px;letter-spacing:5px}
.quote{font-style:italic;font-size:13px;line-height:26px;color:#444}
.card-side .quote{font-size:11px;line-height:22px}
.read-more{display:block;margin-top:12px;color:var(--navy);font-weight:700;font-size:12px}
.card-side .read-more{font-size:11px}
.pager{position:absolute;top:478px;left:561px;display:flex;gap:6px}
.pager span{width:34px;height:34px;border:1.5px solid #555;border-radius:50%;display:flex;align-items:center;justify-content:center}

/* specialties */
.specialties{top:1080px;height:464px;background:linear-gradient(90deg,var(--navy) 0%,#0a5fb5 55%,var(--navy) 100%)}
.specialties-photo{position:absolute;left:560px;top:0;width:400px;height:464px;background:radial-gradient(circle,rgba(123,173,215,.3),rgba(0,84,170,0) 70%)}
.specialties-title{position:absolute;top:86px;width:100%;text-align:center;font-size:30px;color:var(--white)}
.spec{position:absolute;top:183px;width:200px;text-align:center;color:var(--white);font-weight:700;font-size:18px}
.spec-ring{width:156px;height:156px;margin:0 auto 18px;border-radius:50%;background:var(--white);border:6px solid var(--white);box-shadow:inset 0 0 0 4px var(--navy);display:flex;align-items:center;justify-content:center}

/* app */
.app{top:1544px;height:534px}
.app-title{position:absolute;left:170px;top:97px;font-size:30px;line-height:36px}
.app-copy{position:absolute;left:170px;top:195px;width:400px;font-size:13px;line-height:25px;color:#555}
.stores{position:absolute;left:171px;top:351px;display:flex;gap:8px}
.store{width:115px;height:34px;background:#000;border-radius:4px}
.app-visual{position:absolute;left:646px;top:96px;width:384px;height:330px}
.app-heart{position:absolute;left:100px;top:0;width:284px;height:300px;background:var(--ice);border-radius:140px 140px 140px 40px}
.app-photo{position:absolute;left:0;top:60px;width:266px;height:266px;border-radius:50%;background:linear-gradient(135deg,#5a6e84,var(--aqua) 60%,#7fc7b8)}

/* provider */
.provider{top:2078px;height:466px}
.provider-photo{position:absolute;left:0;top:0;width:612px;height:466px;background:linear-gradient(135deg,#e9e2d6 0%,#c98a46 50%,#d9c6a2 100%)}
.provider-panel{position:absolute;left:577px;top:46px;width:623px;height:374px;background:var(--mist);padding:40px 60px}
.provider-title{font-size:29px;line-height:35px}
.provider-copy{margin-top:26px;font-size:13px;line-height:25px;color:#555}
.btn-light{margin-top:30px;width:140px;height:36px;background:var(--white);color:var(--navy);font-size:12px}

/* partners */
.partners{top:2544px;height:372px}
.partners-title{position:absolute;top:112px;width:100%;text-align:center;font-size:29px}
.partner{position:absolute;top:222px;height:100px;display:flex;align-items:center;justify-content:center}
.partner-mark{width:110px;height:50px;border-radius:6px;background:#d8dde3}
.partner-tile{background:#f5f6f7}

/* join */
.join{top:2916px;height:362px;background:linear-gradient(180deg,var(--cyan) 0%,var(--blue) 60%,var(--navy) 100%)}
.join-title{position:absolute;top:104px;width:100%;text-align:center;font-size:33px;line-height:44px;color:var(--white)}
.btn-join{position:absolute;left:530px;top:219px;width:140px;height:34px;background:var(--ice);color:var(--navy);font-size:11px}

/* footer */
.footer{top:3278px;height:304px}
.social{position:absolute;left:145px;top:68px;display:flex;gap:12px}
.social span{width:46px;height:46px;border:2px solid var(--navy);border-radius:50%}
.footer .brand{position:absolute;left:418px;top:56px;font-size:62px}
.footer .brand-dot{width:44px;height:44px}
.footer-stores{position:absolute;right:145px;top:78px;display:flex;gap:8px}
.nav{position:absolute;top:192px;width:100%;text-align:center;font-weight:600;font-size:15px}
.nav span{margin:0 12px}
.legal{position:absolute;top:240px;width:100%;text-align:center;font-size:12px;color:#555}
</style>
</head>
<body>

<header class="section hero">
  <div class="hero-pattern" role="img" aria-label="Faint line pattern of pets, paws and vet items"></div>
  <div class="brand"><span class="brand-dot"></span>Pawdrena</div>
  <div class="hero-actions">
    <span class="btn btn-solid">Sign up</span>
    <span class="btn btn-outline">Login</span>
  </div>
  <h1 class="heading hero-title">Search for Veterinarians</h1>
  <div class="search">
    <div class="field field-company">Search by Company name <span>▾</span></div>
    <div class="field field-date">Pick the date
      <svg width="9" height="9" viewBox="0 0 9 9"><rect x="0" y="1.5" width="9" height="7.5" rx="1" fill="#333"/></svg></div>
    <span class="btn btn-search">Search</span>
  </div>
  <div class="scroll-notch">
    <svg width="80" height="22" viewBox="0 0 80 22"><path d="M33 9l7 6 7-6" fill="none" stroke="#888" stroke-width="1.5"/></svg>
  </div>
</header>

<section class="section doctors">
  <h2 class="heading doctors-title">Doctors with loyal Patients</h2>

  <article class="card card-side" style="left:0">
    <div class="card-head"><div class="avatar" role="img" aria-label="Doctor portrait"></div>
      <div><div class="doc-name">Ravi Teller</div><div class="doc-city">Harborview</div><div class="stars">★★★★★</div></div></div>
    <p class="quote">"Lorem ipsum dolor sit amet, adipiscing elit, sed do eiusm ut labore et dolore magna suspendisses graus commo</p>
    <span class="read-more">READ MORE</span>
  </article>

  <article class="card card-side" style="left:900px">
    <div class="card-head"><div class="avatar" role="img" aria-label="Doctor portrait"></div>
      <div><div class="doc-name">Mira Castell</div><div class="doc-city">Harborview</div><div class="stars">★★★★★</div></div></div>
    <p class="quote">dolor sit amet, consectetur sed do eiusmod temcididunt olore magna aliqua.is ipsum graus commodo"</p>
  </article>

  <article class="card card-main" style="left:204px">
    <div class="card-head"><div class="avatar" role="img" aria-label="Doctor portrait"></div>
      <div><div class="doc-name">Owen Marsh</div><div class="doc-city">Harborview</div><div class="stars">★★★★★</div></div></div>
    <p class="quote">"Lorem ipsum dolor sit amet, consectetur adipiscing elit, sed do eiusmod temcididunt ut labore et dolore magna aliqua.is ipsum suspendisses graus commodo"</p>
    <span class="read-more">READ MORE</span>
  </article>

  <article class="card card-main" style="left:607px">
    <div class="card-head"><div class="avatar" role="img" aria-label="Doctor portrait"></div>
      <div><div class="doc-name">Lina Castell</div><div class="doc-city">Harborview</div><div class="stars">★★★★★</div></div></div>
    <p class="quote">"Lorem ipsum dolor sit amet, consectetur adipiscing elit, sed do eiusmod temcididunt ut labore et dolore magna aliqua.is ipsum suspendisses graus commodo"</p>
    <span class="read-more">READ MORE</span>
  </article>

  <div class="pager">
    <span><svg width="12" height="12" viewBox="0 0 12 12"><path d="M8 1L3 6l5 5" fill="none" stroke="#333" stroke-width="1.6"/></svg></span>
    <span><svg width="12" height="12" viewBox="0 0 12 12"><path d="M4 1l5 5-5 5" fill="none" stroke="#333" stroke-width="1.6"/></svg></span>
  </div>
</section>

<section class="section specialties">
  <div class="specialties-photo" role="img" aria-label="Blue-tinted photo of a person with a pet"></div>
  <h2 class="heading specialties-title">Top-searched specialties</h2>
  <div class="spec" style="left:122px"><div class="spec-ring">
    <svg width="80" height="80" viewBox="0 0 80 80" fill="none" stroke="#0054AA" stroke-width="2.5"><circle cx="40" cy="22" r="14"/><path d="M30 36v14a10 10 0 0020 0V36"/><circle cx="22" cy="62" r="6"/><path d="M28 62h12"/></svg></div>Sed erspiciatis</div>
  <div class="spec" style="left:374px"><div class="spec-ring">
    <svg width="80" height="80" viewBox="0 0 80 80" fill="none" stroke="#0054AA" stroke-width="2.5"><circle cx="34" cy="22" r="11"/><path d="M14 70V54a20 20 0 0140 0v16"/><path d="M30 58v8M26 62h8"/></svg></div>Nemo enim</div>
  <div class="spec" style="left:626px"><div class="spec-ring">
    <svg width="80" height="80" viewBox="0 0 80 80" fill="none" stroke="#0054AA" stroke-width="2.5"><path d="M28 10h24v18h18v24H52v18H28V52H10V28h18z"/><circle cx="40" cy="44" r="7"/><circle cx="32" cy="32" r="3"/><circle cx="48" cy="32" r="3"/></svg></div>Voluptatem</div>
  <div class="spec" style="left:876px"><div class="spec-ring">
    <svg width="80" height="80" viewBox="0 0 80 80" fill="none" stroke="#0054AA" stroke-width="2.5"><rect x="10" y="12" width="60" height="44" rx="2"/><path d="M10 20h60M28 66h24M40 56v10"/><rect x="20" y="28" width="14" height="18"/><path d="M42 32h18M42 40h18"/></svg></div>Neque porro</div>
</section>

<section class="section app">
  <h2 class="heading app-title">Thousands of providers.<br>One app.</h2>
  <p class="app-copy">Lorem ipsum dolor sit amet, consectetur adipiscing elit, sed do eiusmod tempor incididunt ut labore et dolore magna aliqua. Quis ipsum suspendisse ultrices gravidasus commodo viverra maecenas accumsan lacus vel facilisiorem ipsum dolor sit amet, consectetur adipiscing elit, sed do eiusmod</p>
  <div class="stores">
    <span class="store" role="img" aria-label="App store download badge"></span>
    <span class="store" role="img" aria-label="App store download badge"></span>
  </div>
  <div class="app-visual">
    <div class="app-heart"></div>
    <div class="app-photo" role="img" aria-label="Photo of a hand holding a phone showing the app"></div>
  </div>
</section>

<section class="section provider">
  <div class="provider-photo" role="img" aria-label="Photo of a woman kneeling with a golden retriever by a window"></div>
  <div class="provider-panel">
    <h2 class="heading provider-title">Are you a provider interested<br>in reaching new patients?</h2>
    <p class="provider-copy">Lorem ipsum dolor sit amet, consectetur adipiscing elit, sed do eiusmod tempor incididunt ut labore et dolore magna aliqua. Quis ipsum suspendisse ultrices gravidasus commodo viverra maecenas accumsan lacus vel facilisiorem ipsum dolor sit amet, consectetur adipiscingd do eiusmod tempor</p>
    <span class="btn btn-light">Read more</span>
  </div>
</section>

<section class="section partners">
  <h2 class="heading partners-title">We’re trusted by top health systems</h2>
  <div class="partner" style="left:128px;width:110px"><span class="partner-mark" role="img" aria-label="Partner badge"></span></div>
  <div class="partner partner-tile" style="left:278px;width:206px"><span class="partner-mark" role="img" aria-label="Partner badge"></span></div>
  <div class="partner" style="left:538px;width:110px"><span class="partner-mark" role="img" aria-label="Partner badge"></span></div>
  <div class="partner" style="left:744px;width:116px"><span class="partner-mark" role="img" aria-label="Partner badge"></span></div>
  <div class="partner" style="left:944px;width:110px"><span class="partner-mark" role="img" aria-label="Partner badge"></span></div>
</section>

<section class="section join" role="img" aria-label="Blue-tinted photo of a dog behind the call to action">
  <h2 class="heading join-title">Join us, and help transform<br>healthcare for everyone.</h2>
  <span class="btn btn-join">Join us</span>
</section>

<footer class="section footer">
  <div class="social">
    <span role="img" aria-label="Lumigram profile"></span>
    <span role="img" aria-label="Social profile"></span>
    <span role="img" aria-label="Social profile"></span>
  </div>
  <div class="brand"><span class="brand-dot"></span>Pawdrena</div>
  <div class="footer-stores">
    <span class="store" role="img" aria-label="App store download badge"></span>
    <span class="store" role="img" aria-label="App store download badge"></span>
  </div>
  <nav class="nav">HOME<span>/</span>SIGN UP<span>/</span>REGISTRATION<span>/</span>MY ACCOUNT<span>/</span>RESULTS<span>/</span>VETERINARIAN LOG IN<span>/</span>MORE</nav>
  <p class="legal">© 2021 Veterinary Service.All Rights Reserved &nbsp;|&nbsp; Privacy policy &nbsp;|&nbsp; Terms and Use</p>
</footer>

</body>
</html>
```